Excel Template (Branded)

I have a number of reports that I create in Excel. I would like them to be branded instead of generic. Creating a template that I could use for all of my reports would be ideal. I would like to use the colours and logo of my website tallowfern.ca for branding ideas.

Everyday investors over the age of 18

investment

• Professional design that will be shared with readers and subscribers of my blog
• clean professional design elements

```html
<!DOCTYPE html>
<html lang="en">
<head>
<meta charset="utf-8">
<title>Tallow Fern – 10YR Yield on Cost</title>
<link href="https://fonts.googleapis.com/css2?family=Carlito:wght@400;700&display=swap" rel="stylesheet">
<style>
:root{
  --brand-navy:#3b5a8a;
  --band-green:#a9d18e;
  --row-blue:#dde9f6;
  --rule-blue:#9dc3e6;
  --note-navy:#2f4f8f;
  --ink:#111;
  --page:#fff;
}
*{margin:0;padding:0;box-sizing:border-box}
html,body{width:1200px;height:752px;overflow:hidden;background:var(--page)}
body{font-family:"Carlito",Calibri,Arial,sans-serif;color:var(--ink);position:relative}
.brand{position:absolute;left:138px;top:104px;display:flex;align-items:center;gap:10px}
.brand-dot{width:44px;height:44px;border-radius:50%;background:var(--brand-navy)}
.brand-name{font-size:26px;font-weight:700;color:var(--brand-navy);letter-spacing:.2px}
.report-title{position:absolute;left:530px;top:124px;width:200px;text-align:center;font-weight:700;font-size:9.5px;line-height:13px}
.report,.averages-table{position:absolute;left:130px;width:914px;border-collapse:collapse;table-layout:fixed;font-size:9.5px}
.report{top:162px}
.averages-table{top:587px}
.report td,.averages-table td{white-space:nowrap;overflow:hidden;padding:0 2px;line-height:11px}
.report th{white-space:nowrap;padding:0 2px}
.num{text-align:right}
.txt{text-align:left}
.group-row{height:13px}
.group-row th{background:var(--band-green);font-weight:700;text-align:center;font-size:9.5px;line-height:13px}
.group-row th.blank{background:var(--page)}
.label-row{height:26px}
.label-row th{background:var(--band-green);font-weight:700;vertical-align:bottom;line-height:10px;padding-bottom:2px;font-size:9px}
.label-row th:first-child{border-left:2px solid var(--rule-blue)}
.spacer{height:12px}
.spacer td{background:var(--row-blue);border-left:2px solid var(--rule-blue);border-right:2px solid var(--rule-blue)}
.data tr{height:12px}
.data tr td{border-top:1px solid var(--rule-blue)}
.data tr td:first-child{border-left:2px solid var(--rule-blue)}
.data tr td:last-child{border-right:2px solid var(--rule-blue)}
.data tr:nth-child(even) td{background:var(--row-blue)}
.data tr:last-child td{border-bottom:2px solid var(--rule-blue)}
.data .strong{font-weight:700}
.averages-row{height:12px}
.averages-row td{background:var(--band-green);font-weight:700;border-bottom:2px solid #000}
.note{position:absolute;left:130px;top:611px;width:914px;height:47px;border:1.5px solid var(--note-navy);color:var(--note-navy);font-size:8px;line-height:11px;padding:0 2px;overflow:hidden}
</style>
</head>
<body>
<div class="brand">
  <span class="brand-dot"></span>
  <span class="brand-name">Tallow Fern</span>
</div>
<div class="report-title">10YR-Yield on Cost (YOC)<br>as of 01-01-2021</div>

<table class="report">
  <colgroup>
    <col style="width:58px"><col style="width:195px">
    <col style="width:35px"><col style="width:36px"><col style="width:36px"><col style="width:35px"><col style="width:34px"><col style="width:34px"><col style="width:31px"><col style="width:32px"><col style="width:32px"><col style="width:31px">
    <col style="width:38px"><col style="width:30px">
    <col style="width:42px"><col style="width:38px"><col style="width:45px">
    <col style="width:53px"><col style="width:38px"><col style="width:41px">
  </colgroup>
  <thead>
    <tr class="group-row">
      <th class="blank" colspan="2"></th>
      <th colspan="10">Ten Years of Dividend Growth (Year-by-Year)</th>
      <th colspan="2">Price</th>
      <th colspan="3">Yield</th>
      <th colspan="3">Total Return</th>
    </tr>
    <tr class="label-row">
      <th class="txt">Symbol</th><th class="txt">Company</th>
      <th class="num">2011</th><th class="num">2012</th><th class="num">2013</th><th class="num">2014</th><th class="num">2015</th><th class="num">2016</th><th class="num">2017</th><th class="num">2018</th><th class="num">2019</th><th class="num">2020</th>
      <th class="num">$'11</th><th class="num">$'21</th>
      <th class="num">YLD '11</th><th class="num">YLD '21</th><th class="num">10Y YOC</th>
      <th class="num">CAGR<br>10Y TR</th><th class="num">CAGR<br>10Y DG</th><th class="num">CAGR<br>10Y PG</th>
    </tr>
  </thead>
  <tbody>
    <tr class="spacer"><td colspan="20"></td></tr>
  </tbody>
  <tbody class="data">
    <tr><td>NGU-N</td><td>Northgate Utility Holdings</td><td class="num">0.880</td><td class="num">1.000</td><td class="num">1.150</td><td class="num">1.280</td><td class="num">1.410</td><td class="num">1.550</td><td class="num">1.740</td><td class="num">1.880</td><td class="num">2.010</td><td class="num">1.990</td><td class="num">$13</td><td class="num">$ 49</td><td class="num">7.0%</td><td class="num">4.0%</td><td class="num strong">15.9%</td><td class="num strong">14.5%</td><td class="num strong">8.5%</td><td class="num strong">11.5%</td></tr>
    <tr><td>NGU-N</td><td>Northgate Utility Holdings</td><td class="num">0.880</td><td class="num">1.000</td><td class="num">1.150</td><td class="num">1.280</td><td class="num">1.410</td><td class="num">1.550</td><td class="num">1.740</td><td class="num">1.880</td><td class="num">2.010</td><td class="num">1.990</td><td class="num">$13</td><td class="num">$ 49</td><td class="num">7.0%</td><td class="num">4.0%</td><td class="num strong">15.9%</td><td class="num strong">14.5%</td><td class="num strong">8.5%</td><td class="num strong">11.5%</td></tr>
    <tr><td>NGU-N</td><td>Northgate Utility Holdings</td><td class="num">0.880</td><td class="num">1.000</td><td class="num">1.150</td><td class="num">1.280</td><td class="num">1.410</td><td class="num">1.550</td><td class="num">1.740</td><td class="num">1.880</td><td class="num">2.010</td><td class="num">1.990</td><td class="num">$13</td><td class="num">$ 49</td><td class="num">7.0%</td><td class="num">4.0%</td><td class="num strong">15.9%</td><td class="num strong">14.5%</td><td class="num strong">8.5%</td><td class="num strong">11.5%</td></tr>
    <tr><td>NGU-N</td><td>Northgate Utility Holdings</td><td class="num">0.880</td><td class="num">1.000</td><td class="num">1.150</td><td class="num">1.280</td><td class="num">1.410</td><td class="num">1.550</td><td class="num">1.740</td><td class="num">1.880</td><td class="num">2.010</td><td class="num">1.990</td><td class="num">$13</td><td class="num">$ 49</td><td class="num">7.0%</td><td class="num">4.0%</td><td class="num strong">15.9%</td><td class="num strong">14.5%</td><td class="num strong">8.5%</td><td class="num strong">11.5%</td></tr>
    <tr><td>NGU-N</td><td>Northgate Utility Holdings</td><td class="num">0.880</td><td class="num">1.000</td><td class="num">1.150</td><td class="num">1.280</td><td class="num">1.410</td><td class="num">1.550</td><td class="num">1.740</td><td class="num">1.880</td><td class="num">2.010</td><td class="num">1.990</td><td class="num">$13</td><td class="num">$ 49</td><td class="num">7.0%</td><td class="num">4.0%</td><td class="num strong">15.9%</td><td class="num strong">14.5%</td><td class="num strong">8.5%</td><td class="num strong">11.5%</td></tr>
    <tr><td>NGU-N</td><td>Northgate Utility Holdings</td><td class="num">0.880</td><td class="num">1.000</td><td class="num">1.150</td><td class="num">1.280</td><td class="num">1.410</td><td class="num">1.550</td><td class="num">1.740</td><td class="num">1.880</td><td class="num">2.010</td><td class="num">1.990</td><td class="num">$13</td><td class="num">$ 49</td><td class="num">7.0%</td><td class="num">4.0%</td><td class="num strong">15.9%</td><td class="num strong">14.5%</td><td class="num strong">8.5%</td><td class="num strong">11.5%</td></tr>
    <tr><td>NGU-N</td><td>Northgate Utility Holdings</td><td class="num">0.880</td><td class="num">1.000</td><td class="num">1.150</td><td class="num">1.280</td><td class="num">1.410</td><td class="num">1.550</td><td class="num">1.740</td><td class="num">1.880</td><td class="num">2.010</td><td class="num">1.990</td><td class="num">$13</td><td class="num">$ 49</td><td class="num">7.0%</td><td class="num">4.0%</td><td class="num strong">15.9%</td><td class="num strong">14.5%</td><td class="num strong">8.5%</td><td class="num strong">11.5%</td></tr>
    <tr><td>NGU-N</td><td>Northgate Utility Holdings</td><td class="num">0.880</td><td class="num">1.000</td><td class="num">1.150</td><td class="num">1.280</td><td class="num">1.410</td><td class="num">1.550</td><td class="num">1.740</td><td class="num">1.880</td><td class="num">2.010</td><td class="num">1.990</td><td class="num">$13</td><td class="num">$ 49</td><td class="num">7.0%</td><td class="num">4.0%</td><td class="num strong">15.9%</td><td class="num strong">14.5%</td><td class="num strong">8.5%</td><td class="num strong">11.5%</td></tr>
    <tr><td>NGU-N</td><td>Northgate Utility Holdings</td><td class="num">0.880</td><td class="num">1.000</td><td class="num">1.150</td><td class="num">1.280</td><td class="num">1.410</td><td class="num">1.550</td><td class="num">1.740</td><td class="num">1.880</td><td class="num">2.010</td><td class="num">1.990</td><td class="num">$13</td><td class="num">$ 49</td><td class="num">7.0%</td><td class="num">4.0%</td><td class="num strong">15.9%</td><td class="num strong">14.5%</td><td class="num strong">8.5%</td><td class="num strong">11.5%</td></tr>
    <tr><td>NGU-N</td><td>Northgate Utility Holdings</td><td class="num">0.880</td><td class="num">1.000</td><td class="num">1.150</td><td class="num">1.280</td><td class="num">1.410</td><td class="num">1.550</td><td class="num">1.740</td><td class="num">1.880</td><td class="num">2.010</td><td class="num">1.990</td><td class="num">$13</td><td class="num">$ 49</td><td class="num">7.0%</td><td class="num">4.0%</td><td class="num strong">15.9%</td><td class="num strong">14.5%</td><td class="num strong">8.5%</td><td class="num strong">11.5%</td></tr>
    <tr><td>NGU-N</td><td>Northgate Utility Holdings</td><td class="num">0.880</td><td class="num">1.000</td><td class="num">1.150</td><td class="num">1.280</td><td class="num">1.410</td><td class="num">1.550</td><td class="num">1.740</td><td class="num">1.880</td><td class="num">2.010</td><td class="num">1.990</td><td class="num">$13</td><td class="num">$ 49</td><td class="num">7.0%</td><td class="num">4.0%</td><td class="num strong">15.9%</td><td class="num strong">14.5%</td><td class="num strong">8.5%</td><td class="num strong">11.5%</td></tr>
    <tr><td>NGU-N</td><td>Northgate Utility Holdings</td><td class="num">0.880</td><td class="num">1.000</td><td class="num">1.150</td><td class="num">1.280</td><td class="num">1.410</td><td class="num">1.550</td><td class="num">1.740</td><td class="num">1.880</td><td class="num">2.010</td><td class="num">1.990</td><td class="num">$13</td><td class="num">$ 49</td><td class="num">7.0%</td><td class="num">4.0%</td><td class="num strong">15.9%</td><td class="num strong">14.5%</td><td class="num strong">8.5%</td><td class="num strong">11.5%</td></tr>
    <tr><td>NGU-N</td><td>Northgate Utility Holdings</td><td class="num">0.880</td><td class="num">1.000</td><td class="num">1.150</td><td class="num">1.280</td><td class="num">1.410</td><td class="num">1.550</td><td class="num">1.740</td><td class="num">1.880</td><td class="num">2.010</td><td class="num">1.990</td><td class="num">$13</td><td class="num">$ 49</td><td class="num">7.0%</td><td class="num">4.0%</td><td class="num strong">15.9%</td><td class="num strong">14.5%</td><td class="num strong">8.5%</td><td class="num strong">11.5%</td></tr>
    <tr><td>NGU-N</td><td>Northgate Utility Holdings</td><td class="num">0.880</td><td class="num">1.000</td><td class="num">1.150</td><td class="num">1.280</td><td class="num">1.410</td><td class="num">1.550</td><td class="num">1.740</td><td class="num">1.880</td><td class="num">2.010</td><td class="num">1.990</td><td class="num">$13</td><td class="num">$ 49</td><td class="num">7.0%</td><td class="num">4.0%</td><td class="num strong">15.9%</td><td class="num strong">14.5%</td><td class="num strong">8.5%</td><td class="num strong">11.5%</td></tr>
    <tr><td>NGU-N</td><td>Northgate Utility Holdings</td><td class="num">0.880</td><td class="num">1.000</td><td class="num">1.150</td><td class="num">1.280</td><td class="num">1.410</td><td class="num">1.550</td><td class="num">1.740</td><td class="num">1.880</td><td class="num">2.010</td><td class="num">1.990</td><td class="num">$13</td><td class="num">$ 49</td><td class="num">7.0%</td><td class="num">4.0%</td><td class="num strong">15.9%</td><td class="num strong">14.5%</td><td class="num strong">8.5%</td><td class="num strong">11.5%</td></tr>
    <tr><td>NGU-N</td><td>Northgate Utility Holdings</td><td class="num">0.880</td><td class="num">1.000</td><td class="num">1.150</td><td class="num">1.280</td><td class="num">1.410</td><td class="num">1.550</td><td class="num">1.740</td><td class="num">1.880</td><td class="num">2.010</td><td class="num">1.990</td><td class="num">$13</td><td class="num">$ 49</td><td class="num">7.0%</td><td class="num">4.0%</td><td class="num strong">15.9%</td><td class="num strong">14.5%</td><td class="num strong">8.5%</td><td class="num strong">11.5%</td></tr>
    <tr><td>NGU-N</td><td>Northgate Utility Holdings</td><td class="num">0.880</td><td class="num">1.000</td><td class="num">1.150</td><td class="num">1.280</td><td class="num">1.410</td><td class="num">1.550</td><td class="num">1.740</td><td class="num">1.880</td><td class="num">2.010</td><td class="num">1.990</td><td class="num">$13</td><td class="num">$ 49</td><td class="num">7.0%</td><td class="num">4.0%</td><td class="num strong">15.9%</td><td class="num strong">14.5%</td><td class="num strong">8.5%</td><td class="num strong">11.5%</td></tr>
    <tr><td>NGU-N</td><td>Northgate Utility Holdings</td><td class="num">0.880</td><td class="num">1.000</td><td class="num">1.150</td><td class="num">1.280</td><td class="num">1.410</td><td class="num">1.550</td><td class="num">1.740</td><td class="num">1.880</td><td class="num">2.010</td><td class="num">1.990</td><td class="num">$13</td><td class="num">$ 49</td><td class="num">7.0%</td><td class="num">4.0%</td><td class="num strong">15.9%</td><td class="num strong">14.5%</td><td class="num strong">8.5%</td><td class="num strong">11.5%</td></tr>
    <tr><td>NGU-N</td><td>Northgate Utility Holdings</td><td class="num">0.880</td><td class="num">1.000</td><td class="num">1.150</td><td class="num">1.280</td><td class="num">1.410</td><td class="num">1.550</td><td class="num">1.740</td><td class="num">1.880</td><td class="num">2.010</td><td class="num">1.990</td><td class="num">$13</td><td class="num">$ 49</td><td class="num">7.0%</td><td class="num">4.0%</td><td class="num strong">15.9%</td><td class="num strong">14.5%</td><td class="num strong">8.5%</td><td class="num strong">11.5%</td></tr>
    <tr><td>NGU-N</td><td>Northgate Utility Holdings</td><td class="num">0.880</td><td class="num">1.000</td><td class="num">1.150</td><td class="num">1.280</td><td class="num">1.410</td><td class="num">1.550</td><td class="num">1.740</td><td class="num">1.880</td><td class="num">2.010</td><td class="num">1.990</td><td class="num">$13</td><td class="num">$ 49</td><td class="num">7.0%</td><td class="num">4.0%</td><td class="num strong">15.9%</td><td class="num strong">14.5%</td><td class="num strong">8.5%</td><td class="num strong">11.5%</td></tr>
    <tr><td>NGU-N</td><td>Northgate Utility Holdings</td><td class="num">0.880</td><td class="num">1.000</td><td class="num">1.150</td><td class="num">1.280</td><td class="num">1.410</td><td class="num">1.550</td><td class="num">1.740</td><td class="num">1.880</td><td class="num">2.010</td><td class="num">1.990</td><td class="num">$13</td><td class="num">$ 49</td><td class="num">7.0%</td><td class="num">4.0%</td><td class="num strong">15.9%</td><td class="num strong">14.5%</td><td class="num strong">8.5%</td><td class="num strong">11.5%</td></tr>
    <tr><td>NGU-N</td><td>Northgate Utility Holdings</td><td class="num">0.880</td><td class="num">1.000</td><td class="num">1.150</td><td class="num">1.280</td><td class="num">1.410</td><td class="num">1.550</td><td class="num">1.740</td><td class="num">1.880</td><td class="num">2.010</td><td class="num">1.990</td><td class="num">$13</td><td class="num">$ 49</td><td class="num">7.0%</td><td class="num">4.0%</td><td class="num strong">15.9%</td><td class="num strong">14.5%</td><td class="num strong">8.5%</td><td class="num strong">11.5%</td></tr>
    <tr><td>NGU-N</td><td>Northgate Utility Holdings</td><td class="num">0.880</td><td class="num">1.000</td><td class="num">1.150</td><td class="num">1.280</td><td class="num">1.410</td><td class="num">1.550</td><td class="num">1.740</td><td class="num">1.880</td><td class="num">2.010</td><td class="num">1.990</td><td class="num">$13</td><td class="num">$ 49</td><td class="num">7.0%</td><td class="num">4.0%</td><td class="num strong">15.9%</td><td class="num strong">14.5%</td><td class="num strong">8.5%</td><td class="num strong">11.5%</td></tr>
    <tr><td>NGU-N</td><td>Northgate Utility Holdings</td><td class="num">0.880</td><td class="num">1.000</td><td class="num">1.150</td><td class="num">1.280</td><td class="num">1.410</td><td class="num">1.550</td><td class="num">1.740</td><td class="num">1.880</td><td class="num">2.010</td><td class="num">1.990</td><td class="num">$13</td><td class="num">$ 49</td><td class="num">7.0%</td><td class="num">4.0%</td><td class="num strong">15.9%</td><td class="num strong">14.5%</td><td class="num strong">8.5%</td><td class="num strong">11.5%</td></tr>
    <tr><td>NGU-N</td><td>Northgate Utility Holdings</td><td class="num">0.880</td><td class="num">1.000</td><td class="num">1.150</td><td class="num">1.280</td><td class="num">1.410</td><td class="num">1.550</td><td class="num">1.740</td><td class="num">1.880</td><td class="num">2.010</td><td class="num">1.990</td><td class="num">$13</td><td class="num">$ 49</td><td class="num">7.0%</td><td class="num">4.0%</td><td class="num strong">15.9%</td><td class="num strong">14.5%</td><td class="num strong">8.5%</td><td class="num strong">11.5%</td></tr>
    <tr><td>NGU-N</td><td>Northgate Utility Holdings</td><td class="num">0.880</td><td class="num">1.000</td><td class="num">1.150</td><td class="num">1.280</td><td class="num">1.410</td><td class="num">1.550</td><td class="num">1.740</td><td class="num">1.880</td><td class="num">2.010</td><td class="num">1.990</td><td class="num">$13</td><td class="num">$ 49</td><td class="num">7.0%</td><td class="num">4.0%</td><td class="num strong">15.9%</td><td class="num strong">14.5%</td><td class="num strong">8.5%</td><td class="num strong">11.5%</td></tr>
    <tr><td>NGU-N</td><td>Northgate Utility Holdings</td><td class="num">0.880</td><td class="num">1.000</td><td class="num">1.150</td><td class="num">1.280</td><td class="num">1.410</td><td class="num">1.550</td><td class="num">1.740</td><td class="num">1.880</td><td class="num">2.010</td><td class="num">1.990</td><td class="num">$13</td><td class="num">$ 49</td><td class="num">7.0%</td><td class="num">4.0%</td><td class="num strong">15.9%</td><td class="num strong">14.5%</td><td class="num strong">8.5%</td><td class="num strong">11.5%</td></tr>
    <tr><td>NGU-N</td><td>Northgate Utility Holdings</td><td class="num">0.880</td><td class="num">1.000</td><td class="num">1.150</td><td class="num">1.280</td><td class="num">1.410</td><td class="num">1.550</td><td class="num">1.740</td><td class="num">1.880</td><td class="num">2.010</td><td class="num">1.990</td><td class="num">$13</td><td class="num">$ 49</td><td class="num">7.0%</td><td class="num">4.0%</td><td class="num strong">15.9%</td><td class="num strong">14.5%</td><td class="num strong">8.5%</td><td class="num strong">11.5%</td></tr>
    <tr><td>NGU-N</td><td>Northgate Utility Holdings</td><td class="num">0.880</td><td class="num">1.000</td><td class="num">1.150</td><td class="num">1.280</td><td class="num">1.410</td><td class="num">1.550</td><td class="num">1.740</td><td class="num">1.880</td><td class="num">2.010</td><td class="num">1.990</td><td class="num">$13</td><td class="num">$ 49</td><td class="num">7.0%</td><td class="num">4.0%</td><td class="num strong">15.9%</td><td class="num strong">14.5%</td><td class="num strong">8.5%</td><td class="num strong">11.5%</td></tr>
    <tr><td>NGU-N</td><td>Northgate Utility Holdings</td><td class="num">0.880</td><td class="num">1.000</td><td class="num">1.150</td><td class="num">1.280</td><td class="num">1.410</td><td class="num">1.550</td><td class="num">1.740</td><td class="num">1.880</td><td class="num">2.010</td><td class="num">1.990</td><td class="num">$13</td><td class="num">$ 49</td><td class="num">7.0%</td><td class="num">4.0%</td><td class="num strong">15.9%</td><td class="num strong">14.5%</td><td class="num strong">8.5%</td><td class="num strong">11.5%</td></tr>
    <tr><td>NGU-N</td><td>Northgate Utility Holdings</td><td class="num">0.880</td><td class="num">1.000</td><td class="num">1.150</td><td class="num">1.280</td><td class="num">1.410</td><td class="num">1.550</td><td class="num">1.740</td><td class="num">1.880</td><td class="num">2.010</td><td class="num">1.990</td><td class="num">$13</td><td class="num">$ 49</td><td class="num">7.0%</td><td class="num">4.0%</td><td class="num strong">15.9%</td><td class="num strong">14.5%</td><td class="num strong">8.5%</td><td class="num strong">11.5%</td></tr>
  </tbody>
</table>

<table class="averages-table">
  <colgroup>
    <col style="width:58px"><col style="width:195px">
    <col style="width:35px"><col style="width:36px"><col style="width:36px"><col style="width:35px"><col style="width:34px"><col style="width:34px"><col style="width:31px"><col style="width:32px"><col style="width:32px"><col style="width:31px">
    <col style="width:38px"><col style="width:30px">
    <col style="width:42px"><col style="width:38px"><col style="width:45px">
    <col style="width:53px"><col style="width:38px"><col style="width:41px">
  </colgroup>
  <tbody>
    <tr class="averages-row">
      <td colspan="2" class="txt">Averages</td>
      <td colspan="12"></td>
      <td class="num">7.0%</td><td class="num">4.0%</td><td class="num">15.9%</td>
      <td class="num">14.5%</td><td class="num">8.5%</td><td class="num">11.5%</td>
    </tr>
  </tbody>
</table>

<div class="note">The List' is in YOC order. What kind of a yield (on dividends alone) can you expect after ten years? Making YOC the 'The List' is in YOC order. What kind of a yield (on dividends alone) can you expect after ten years? Making YOC the primary<br>focus when evaluating the success or failure of your portfolio's<br>ability to meet your income needs over time is a good approach. Planning the yield you need in the future based on today's portfolio value tells you how long until you can retire. It can make all<br>the difference in getting started and sticking with your plan. focus when evaluating the success or failure of your portfolio's</div>
</body>
</html>
```